BUsiness Card

We need a unique business card design for a new aesthetic practice, Meadowlark Skin & Vitality, P.A. The reverse of the card should be an appointment card.

```html
<!DOCTYPE html>
<html lang="en">
<head>
<meta charset="utf-8">
<title>Meadowlark Skin &amp; Vitality – Business Card</title>
<link rel="stylesheet" href="https://fonts.googleapis.com/css2?family=Cinzel:wght@400;600&family=Raleway:wght@500;600&display=swap">
<style>
  :root {
    --navy: #124766;
    --teal: #22a89e;
    --paper: #ffffff;
    --paper-shade: #eceef0;
    --ink: #1b1b1b;
    --backdrop: #eef0f0;
  }
  * { margin: 0; padding: 0; box-sizing: border-box; }
  html, body { width: 1200px; height: 933px; overflow: hidden; }
  body { background: var(--backdrop); position: relative; }

  .card {
    position: absolute;
    top: 169px;
    width: 340px;
    height: 595px;
    overflow: hidden;
    background: var(--paper);
    box-shadow: 0 6px 18px rgba(0,0,0,0.12);
  }
  .card--appointment { left: 215px; }
  .card--contact { left: 645px; }

  .card__art { position: absolute; inset: 0; width: 100%; height: 100%; }

  .texture {
    position: absolute; inset: 0;
    background: linear-gradient(160deg, var(--paper) 0%, var(--paper-shade) 55%, var(--paper) 100%);
  }

  /* Appointment side */
  .appointment__mark {
    position: absolute; left: 112px; top: 160px;
    width: 66px; height: 66px; border-radius: 50%;
    background: var(--navy);
  }
  .appointment__title {
    position: absolute; left: 40px; top: 242px; width: 210px;
    text-align: center;
    font-family: "Cinzel", serif; font-weight: 400;
    font-size: 25px; color: var(--teal); letter-spacing: 0.5px;
  }
  .appointment__line {
    position: absolute; left: 52px; width: 186px; height: 2px;
    background: var(--ink);
  }
  .appointment__line--first { top: 300px; }
  .appointment__line--second { top: 340px; }

  /* Contact side */
  .contact { position: absolute; inset: 0; text-align: center; }
  .brand__mark {
    position: absolute; left: 132px; top: 58px;
    width: 76px; height: 76px; border-radius: 50%;
    background: var(--navy);
  }
  .brand__name {
    position: absolute; left: 0; right: 0; top: 146px;
    font-family: "Cinzel", serif; font-weight: 600; color: var(--navy);
    line-height: 1.1;
  }
  .brand__name-main { display: block; font-size: 36px; }
  .brand__name-sub { display: block; font-size: 14px; letter-spacing: 2px; }

  .person__name {
    position: absolute; left: 0; right: 0; top: 262px;
    font-family: "Cinzel", serif; font-weight: 400;
    font-size: 27px; color: var(--navy);
  }
  .person__role {
    position: absolute; left: 0; right: 0; top: 298px;
    font-family: "Cinzel", serif; font-size: 15px; color: var(--ink); letter-spacing: 1px;
  }
  .divider {
    position: absolute; left: 135px; width: 70px; height: 2px;
    background: var(--navy); border-radius: 50%;
  }
  .divider--upper { top: 338px; }
  .divider--lower { top: 432px; }

  .details {
    position: absolute; left: 0; right: 0;
    font-family: "Raleway", sans-serif; font-weight: 600;
    font-size: 14px; color: var(--ink); line-height: 1.35;
  }
  .details--reach { top: 362px; }
  .details--address { top: 462px; }
</style>
</head>
<body>

  <section class="card card--appointment" aria-label="Appointment card">
    <svg class="card__art" viewBox="0 0 340 595" role="img" aria-label="Navy and teal curved bands framing a soft grey wave texture">
      <defs>
        <linearGradient id="paperShade" x1="0" y1="0" x2="1" y2="1">
          <stop offset="0" stop-color="#ffffff"/>
          <stop offset="0.55" stop-color="#eceef0"/>
          <stop offset="1" stop-color="#ffffff"/>
        </linearGradient>
      </defs>
      <rect width="340" height="595" fill="#124766"/>
      <ellipse cx="150" cy="300" rx="262" ry="246" fill="#22a89e"/>
      <ellipse cx="128" cy="300" rx="246" ry="222" fill="url(#paperShade)"/>
    </svg>
    <div class="appointment__mark" aria-hidden="true"></div>
    <h2 class="appointment__title">APPOINTMENT</h2>
    <div class="appointment__line appointment__line--first"></div>
    <div class="appointment__line appointment__line--second"></div>
  </section>

  <section class="card card--contact" aria-label="Contact card">
    <div class="texture" role="img" aria-label="Soft grey wave texture"></div>
    <div class="contact">
      <div class="brand__mark" aria-hidden="true"></div>
      <h1 class="brand__name">
        <span class="brand__name-main">MEADOWLARK</span>
        <span class="brand__name-sub">SKIN &amp; VITALITY</span>
      </h1>
      <p class="person__name">JORDAN AVERY</p>
      <p class="person__role">OWNER</p>
      <div class="divider divider--upper"></div>
      <p class="details details--reach">Call +1 555-014-2290<br>www.meadowlark-skin.com</p>
      <div class="divider divider--lower"></div>
      <p class="details details--address">870 Harbor Lane, Suite 114<br>Fairhaven, Maryland</p>
    </div>
  </section>

</body>
</html>
```